Book Cover design for Kindle and print book.

I’m looking for a unique and fresh approach for this book cover design because the content has a unique and fresh approach. For example I don't want a design that has steps, bulls eyes, targets or trophies. Because it incorporates some of the spiritual elements of goal setting I’d like it to encompass my signature purple colour #330066.

Think about people who want to set unrealistic or aspirational goals that will change the world - rather than people who want to achieve a simple goal.

I want a cover that will work for Kindle and for a print book, and, possibly later, a workbook.

NB My company logo is not intended to go onto the book, it's for your information only. However, an ISBN number will be included.

Target Market(s)

20-60 year old professional men and women who are motivated and want to achieve huge, aspirational goals while enjoying the journey.

Font styles to use
Serif
Sans Serif
Other font styles liked:
• I use Agenda in my manuals, but this isn't essential.

Requirements
Must have
• I prefer rounded shapes rather than sharp angles - but I'm pretty open to new designs. I also prefer font to be set in a combination of upper and lower case letters.
Nice to have
• purple colour #330066 if possible. I don't expect this to be all over the cover. Taking a quick look at my website http://lanternquay.example.nz might help. Otherwise I'm open to colour, but not a fan of green.
• I like the cleverness and simplicity of Born to Linger, (http://www.pelicanreads.example/Born-Linger-Thrive-Rivals-released/dp/Q77K42WX19/ref=sr_1_4?s=books&ie=UTF8&qid=1458845324&sr=1-4&keywords=Born+to+Linger) In fact all the book covers of Rolf and Ivan Marsh's books are impressive.
Should not have
• Bulls eyes, steps, targets or other symbols traditionally associated with goal setting.

```html
<!DOCTYPE html>
<html lang="en">
<head>
<meta charset="utf-8">
<title>Goal Setting – Book Cover Wrap</title>
<link rel="stylesheet" href="https://fonts.googleapis.com/css2?family=Marcellus&family=Josefin+Sans:wght@300;400&family=Open+Sans:wght@400;700&family=Ubuntu:wght@500;700&display=swap">
<style>
  :root {
    --mist-white: #f7fbfa;
    --mist-aqua: #cfe9e6;
    --sea-teal: #6fa9a6;
    --deep-teal: #2f5f60;
    --royal-purple: #330066;
    --bright-violet: #8a2be2;
    --ink: #1f1f24;
    --sun-core: #fff3c8;
    --sun-gold: #f5b43a;
    --sun-orange: #e8731e;
    --white: #ffffff;
  }
  * { margin: 0; padding: 0; box-sizing: border-box; }
  html, body { width: 1200px; height: 870px; overflow: hidden; background: var(--mist-white); }
  .cover-wrap {
    position: relative;
    width: 1200px; height: 870px;
    overflow: hidden;
    background:
      radial-gradient(ellipse 520px 420px at 300px 380px, rgba(255,255,255,0.95), rgba(255,255,255,0) 75%),
      radial-gradient(ellipse 480px 380px at 910px 400px, rgba(255,255,255,0.95), rgba(255,255,255,0) 75%),
      linear-gradient(180deg, #a6d3cf 0%, var(--mist-aqua) 12%, var(--mist-white) 35%, var(--mist-white) 62%, var(--mist-aqua) 76%, var(--sea-teal) 88%, var(--deep-teal) 100%);
  }
  .sun-disc { position: absolute; }
  .sun-disc--back { left: 112px; top: -215px; width: 328px; height: 328px; }
  .sun-disc--front { left: 733px; top: 259px; width: 350px; height: 352px; }

  /* Back cover */
  .back-blurb {
    position: absolute; left: 65px; top: 147px; width: 451px;
    font-family: "Open Sans", sans-serif;
    font-size: 15.6px; line-height: 21.7px; letter-spacing: -0.1px; color: var(--ink);
    text-align: justify;
  }
  .back-blurb p { margin-bottom: 21.7px; }
  .back-blurb strong { font-weight: 700; }

  /* Spine */
  .spine-title {
    position: absolute; left: 568px; top: 198px;
    writing-mode: vertical-rl;
    font-family: "Marcellus", serif;
    font-size: 42px; letter-spacing: 6px; line-height: 1;
    color: var(--bright-violet);
  }
  .spine-author {
    position: absolute; left: 584px; top: 596px;
    writing-mode: vertical-rl;
    font-family: "Ubuntu", sans-serif; font-weight: 700;
    font-size: 21px; line-height: 1; color: var(--ink);
  }

  /* Front cover */
  .front-title {
    position: absolute; left: 655px; top: 74px; width: 530px;
    font-family: "Marcellus", serif; font-weight: 400;
    font-size: 74px; line-height: 1; letter-spacing: 1px; white-space: nowrap;
    background: linear-gradient(90deg, var(--bright-violet) 0%, #6a1bb8 60%, var(--royal-purple) 100%);
    -webkit-background-clip: text; background-clip: text; color: transparent;
  }
  .front-subtitle {
    position: absolute; left: 640px; top: 150px; width: 540px;
    text-align: center;
    font-family: "Josefin Sans", sans-serif; font-weight: 300;
    font-size: 30px; line-height: 38px; letter-spacing: 2.4px;
    color: var(--royal-purple);
  }
  .front-tagline {
    position: absolute; left: 693px; top: 662px; width: 430px;
    text-align: center;
    font-family: "Josefin Sans", sans-serif; font-weight: 300;
    font-size: 23px; line-height: 37px; color: var(--ink);
  }
  .front-tagline .method { font-family: "Open Sans", sans-serif; font-size: 24px; letter-spacing: -0.5px; }
  .front-author {
    position: absolute; left: 745px; top: 796px; width: 340px;
    text-align: center;
    font-family: "Ubuntu", sans-serif; font-weight: 700;
    font-size: 32px; color: var(--white);
  }
</style>
</head>
<body>
<main class="cover-wrap">
  <svg class="sun-disc sun-disc--back" viewBox="0 0 100 100" role="img" aria-label="Glowing orange sun disc with golden swirl pattern">
    <defs>
      <radialGradient id="sunGlowBack" cx="50%" cy="50%" r="50%">
        <stop offset="0%" stop-color="var(--sun-core)"/>
        <stop offset="45%" stop-color="var(--sun-gold)"/>
        <stop offset="100%" stop-color="var(--sun-orange)"/>
      </radialGradient>
    </defs>
    <circle cx="50" cy="50" r="50" fill="url(#sunGlowBack)"/>
  </svg>

  <section class="back-blurb">
    <p>If you’ve ever fallen short of a dream - (and let’s be honest - who hasn’t?) then this book was written for you.</p>
    <p>By working through the 7 principles that form the <strong>R.A.D.I.A.N.T.</strong> goal setting method you’ll discover how to fill the gaps that other planning models leave open. Use the method to set wildly ambitious goals; goals that will stretch you to learn and expand while enjoying the most wonderful adventure on the road to living your vision.</p>
    <p><strong>R.A.D.I.A.N.T.</strong> Goal setting will reveal why some goals can feel as if you’re dragging yourself towards them an inch at a time, uphill, into a headwind - in the rain! You discover how to choose goals that, while challenging you, also feel light and joyful.</p>
    <p>The <strong>R.A.D.I.A.N.T.</strong> method blends the newest findings in brain and behaviour research with timeless and spiritual insight. It’s full of stories that illuminate each principle.</p>
    <p>Serena Whitlow is an internationally respected Author, Senior Facilitator and Coach/Mentor. In this book, she’s drawn on her 20 years of practice to show you what works, as well as what simply doesn’t work to shape the future you want.</p>
  </section>

  <div class="spine-title">GOAL SETTING</div>
  <div class="spine-author">Serena Whitlow</div>

  <h1 class="front-title">GOAL SETTING</h1>
  <p class="front-subtitle">7 Pathways to Reach<br>Extraordinary Heights</p>

  <svg class="sun-disc sun-disc--front" viewBox="0 0 100 100" role="img" aria-label="Radiant orange sun disc with golden swirl pattern and bright white centre">
    <defs>
      <radialGradient id="sunGlowFront" cx="48%" cy="42%" r="55%">
        <stop offset="0%" stop-color="#ffffff"/>
        <stop offset="18%" stop-color="var(--sun-core)"/>
        <stop offset="50%" stop-color="var(--sun-gold)"/>
        <stop offset="100%" stop-color="var(--sun-orange)"/>
      </radialGradient>
    </defs>
    <circle cx="50" cy="50" r="50" fill="url(#sunGlowFront)"/>
  </svg>

  <p class="front-tagline">Using the <span class="method">R.A.D.I.A.N.T.</span> method<br>to shape your future.</p>
  <p class="front-author">Serena Whitlow</p>
</main>
</body>
</html>
```